Business Stationery Branding

This is NOT a logo job. We already have one (attached)

Projects that do not follow the color scheme (see logo) will be rejected immediately.

What I need is for someone to create a modern, clean, simple and minimalist branding for the business.

The designs will be 100% and delivery will include all source & vector files.

What I need are:
1. Business Card
2. Letterhead
3. Envelope
4. Invoice
5. Presentation folder
6. Staff / ID Card
7. Compliments slips
8. Notepad cover
9. Note pad
10. Mug design
11. Pen design

```html
<!DOCTYPE html>
<html lang="en">
<head>
<meta charset="utf-8">
<title>Nala Care Services — Letterhead</title>
<link rel="stylesheet" href="https://fonts.googleapis.com/css2?family=Arimo:wght@400;700&display=swap">
<style>
  :root {
    --backdrop: #ddd5cf;
    --paper: #ffffff;
    --brand-red: #a3303a;
    --ink: #2a2a2a;
    --ink-soft: #555555;
    --band: #1c1c1c;
    --chevron: #d0202a;
    --signature: #e2e2e2;
  }
  * { box-sizing: border-box; margin: 0; padding: 0; }
  html, body { width: 1200px; height: 900px; overflow: hidden; }
  body { background: var(--backdrop); font-family: "Arimo", Arial, sans-serif; color: var(--ink); position: relative; }

  .letterhead {
    position: absolute; left: 296px; top: 20px;
    width: 608px; height: 860px;
    background: var(--paper);
    box-shadow: 0 2px 10px rgba(0,0,0,0.12);
    overflow: hidden;
  }
  .brand-name {
    position: absolute; left: 57px; top: 84px;
    font-size: 22px; font-weight: 700; letter-spacing: 1px;
    color: var(--brand-red);
  }
  .sender-name { position: absolute; left: 57px; top: 140px; font-size: 21px; font-weight: 700; color: var(--brand-red); }
  .sender-role { position: absolute; left: 57px; top: 164px; font-size: 11px; color: var(--ink-soft); }
  .letter-date { position: absolute; right: 58px; top: 170px; font-size: 11px; color: var(--ink-soft); }

  .contact-list { position: absolute; left: 57px; top: 190px; font-size: 11px; line-height: 15px; color: var(--ink-soft); }
  .contact-list div { display: flex; }
  .contact-list dt { width: 60px; }

  .letter-body { position: absolute; left: 57px; top: 278px; width: 496px; font-size: 11.3px; line-height: 15.5px; color: var(--ink); text-align: justify; }
  .letter-body p { margin-bottom: 15px; }

  .signature { position: absolute; left: 57px; top: 652px; width: 110px; height: 34px; }
  .closing-name { position: absolute; left: 57px; top: 690px; font-size: 20px; font-weight: 700; color: var(--ink); }
  .closing-role { position: absolute; left: 57px; top: 713px; font-size: 10px; color: var(--ink-soft); }

  .footer-contacts { position: absolute; left: 57px; right: 40px; top: 762px; display: flex; font-size: 10.5px; line-height: 13px; color: var(--ink-soft); }
  .footer-item { display: flex; align-items: flex-start; gap: 8px; }
  .footer-item svg { margin-top: 5px; flex: none; }
  .footer-item.phone { width: 130px; }
  .footer-item.email { width: 206px; }

  .footer-band { position: absolute; left: 0; bottom: 0; width: 608px; height: 60px; }
</style>
</head>
<body>
  <main class="letterhead">
    <div class="brand-name">NALA CARE SERVICES</div>

    <div class="sender-name">Daniel Okoro</div>
    <div class="sender-role">Graphic Designer</div>
    <div class="letter-date">Date 11 March 2015</div>

    <dl class="contact-list">
      <div><dt>Address</dt><dd>: Harbour Road, Lindenfield 4020</dd></div>
      <div><dt>Web</dt><dd>: www.nalacare.example</dd></div>
      <div><dt>Email</dt><dd>: hello@nalacare.example</dd></div>
      <div><dt>Phone</dt><dd>: 0100 555 0142</dd></div>
    </dl>

    <section class="letter-body">
      <p>Lorem Ipsum is simply dummy text of the printing and typesetting industry. Lorem Ipsum has been the industry's standard dummy text ever since the 1500s, when an unknown printer took a galley of type and scrambled it to</p>
      <p>make a type specimen book. It hasLorem Ipsum is simply dummy text of the printing and typesetting industry. Lorem Ipsum has been the industry's standard dummy text ever since the 1500s, when an</p>
      <p>unknown printer took a galley of type and scrambled it to make a type specimen book. It hasLorem Ipsum is simply dummy text of the printing and typesetting industry. Lorem Ipsum has been the industry's standard dummy text ever since the 1500s, when an unknown printer took a galley of type and scrambled it to make a type</p>
      <p>specimen book. It hasLorem Ipsum is simply dummy text of the printing and typesetting industry. Lorem Ipsum has been the industry's standard dummy text ever since the 1500s, when an unknown printer took a galley of type and scrambled it to make a type specimen book. It hasLorem Ipsum is simply dummy text of the</p>
      <p>printing and typesetting industry. Lorem Ipsum has been the industry's standard dummy text ever since the 1500s, when an unknown printer took a galley of type and scrambled it to make a type specimen book. It has</p>
    </section>

    <svg class="signature" role="img" aria-label="Handwritten signature" viewBox="0 0 110 34">
      <rect x="0" y="0" width="110" height="30" fill="var(--signature)"/>
      <line x1="0" y1="33" x2="110" y2="33" stroke="var(--ink)" stroke-width="1"/>
    </svg>
    <div class="closing-name">Daniel Okoro</div>
    <div class="closing-role">Graphic Designer</div>

    <div class="footer-contacts">
      <div class="footer-item phone">
        <svg width="12" height="12" viewBox="0 0 24 24"><path fill="var(--ink)" d="M6.6 10.8a15.1 15.1 0 0 0 6.6 6.6l2.2-2.2c.3-.3.7-.4 1-.2 1.1.4 2.3.6 3.6.6.6 0 1 .4 1 1V20c0 .6-.4 1-1 1A17 17 0 0 1 3 4c0-.6.4-1 1-1h3.5c.6 0 1 .4 1 1 0 1.3.2 2.5.6 3.6.1.3 0 .7-.2 1z"/></svg>
        <div>0100 555 0187<br>0100 555 0188</div>
      </div>
      <div class="footer-item email">
        <svg width="14" height="11" viewBox="0 0 24 18"><rect x="1" y="1" width="22" height="16" fill="none" stroke="var(--ink)" stroke-width="2"/><path d="M1 1l11 9 11-9" fill="none" stroke="var(--ink)" stroke-width="2"/></svg>
        <div>office@nalacare.example<br>office@nalacare.example</div>
      </div>
      <div class="footer-item address">
        <svg width="10" height="14" viewBox="0 0 20 28"><path fill="var(--ink)" d="M10 0C4.5 0 0 4.5 0 10c0 7.5 10 18 10 18s10-10.5 10-18C20 4.5 15.5 0 10 0zm0 14a4 4 0 1 1 0-8 4 4 0 0 1 0 8z"/></svg>
        <div>12 Mill Lane<br>Lindenfield 4020</div>
      </div>
    </div>

    <svg class="footer-band" viewBox="0 0 608 60" preserveAspectRatio="none">
      <rect x="0" y="8" width="608" height="52" fill="var(--band)"/>
      <polygon points="364,4 490,4 427,60" fill="var(--chevron)"/>
      <polygon points="384,4 470,4 427,42" fill="var(--paper)"/>
    </svg>
  </main>
</body>
</html>
```